Redesign the *Settings* screen for the PelikoZ app.

PelikoZ app is in production, but we need to refresh and redesign the settings screen to be cleaner, easier, more intuitive, and more professional looking.

Project Deadline Extended
Reason: Several designers have requested more time. This will also give time to provide feedback on existing designs.

Requirements
Must have
• Black background, so that the screen is consistent with the rest of the app.

```html
<!DOCTYPE html>
<html lang="en">
<head>
<meta charset="utf-8">
<title>PelikoZ – Settings</title>
<link rel="stylesheet" href="https://fonts.googleapis.com/css2?family=Roboto:wght@400;500&display=swap">
<style>
  :root {
    --page: #111111;
    --screen: #000000;
    --row: #2c2c2c;
    --divider: #1e1e1e;
    --version-strip: #3a3a3a;
    --tabbar: #2a2a2a;
    --text: #ffffff;
    --muted: #9a9a9a;
    --accent: #c4363c;
    --outline: #e2e2e2;
  }
  * { box-sizing: border-box; margin: 0; padding: 0; }
  html, body { width: 1200px; height: 1200px; overflow: hidden; }
  body {
    background: var(--page);
    font-family: "Roboto", Arial, sans-serif;
    color: var(--text);
    position: relative;
  }
  .settings-screen {
    position: absolute;
    left: 274px; top: 19px;
    width: 652px; height: 1162px;
    background: var(--screen);
    display: flex; flex-direction: column;
  }
  .status-bar {
    height: 46px; background: var(--row);
    display: flex; align-items: center; justify-content: space-between;
    padding: 0 14px; font-size: 19px;
    border-bottom: 1px solid var(--divider);
  }
  .status-left, .status-right { display: flex; align-items: center; gap: 8px; width: 200px; }
  .status-right { justify-content: flex-end; }
  .signal { display: flex; gap: 2px; }
  .signal span { width: 10px; height: 10px; border-radius: 50%; border: 1.5px solid #fff; }
  .signal span.on { background: #fff; }
  .battery { width: 38px; height: 16px; border: 1.5px solid #fff; border-radius: 3px; padding: 1.5px; position: relative; }
  .battery::after { content: ""; position: absolute; right: -5px; top: 4px; width: 3px; height: 6px; background: #fff; border-radius: 0 2px 2px 0; }
  .battery i { display: block; height: 100%; background: #fff; border-radius: 1px; }

  .setting-row {
    height: 103px; background: var(--row);
    border-bottom: 1px solid var(--divider);
    display: flex; align-items: center; justify-content: space-between;
    padding: 0 15px 0 14px;
  }
  .setting-label { font-size: 25px; }
  .setting-value { font-size: 25px; font-weight: 500; color: var(--accent); }
  .option-group { display: flex; gap: 23px; }
  .option {
    width: 48px; height: 48px; border-radius: 50%;
    border: 1.5px solid var(--outline);
    display: flex; align-items: center; justify-content: center;
    font-size: 14px; font-weight: 500; color: #fff;
  }
  .option.is-active { background: var(--accent); border-color: var(--accent); }
  .option.info { width: 34px; height: 34px; margin: 7px 0; background: #fff; border: none; color: #111; font-family: Georgia, serif; font-weight: 700; font-size: 20px; }
  .option svg { width: 26px; height: 26px; }

  .link-row {
    height: 67.5px; background: var(--row);
    border-bottom: 1px solid var(--divider);
    display: flex; align-items: center; justify-content: space-between;
    padding: 0 15px 0 14px;
    color: var(--accent); font-size: 23px;
  }
  .link-row svg { width: 10px; height: 24px; }

  .version-strip {
    height: 35px; background: var(--version-strip);
    display: flex; align-items: center; justify-content: center;
    font-size: 15px; color: var(--muted);
  }
  .tab-bar {
    height: 90px; background: var(--tabbar);
    display: flex; justify-content: space-around; align-items: flex-end;
    padding-bottom: 4px;
  }
  .tab { width: 140px; display: flex; flex-direction: column; align-items: center; gap: 2px; font-size: 17px; }
  .tab svg { width: 60px; height: 56px; }
  .tab.is-current { color: var(--accent); }
</style>
</head>
<body>
<main class="settings-screen">
  <div class="status-bar">
    <div class="status-left">
      <div class="signal"><span class="on"></span><span class="on"></span><span class="on"></span><span></span><span></span></div>
      <span>VOLT</span>
      <svg width="22" height="16" viewBox="0 0 22 16"><path d="M2 6a13 13 0 0 1 18 0M5 9a8.5 8.5 0 0 1 12 0M8 12a4 4 0 0 1 6 0" fill="none" stroke="#fff" stroke-width="2"/><circle cx="11" cy="14.5" r="1.5" fill="#fff"/></svg>
    </div>
    <span>4:21 PM</span>
    <div class="status-right">
      <svg width="12" height="20" viewBox="0 0 12 20"><path d="M2 5l8 9-4 4V2l4 4-8 9" fill="none" stroke="#aaa" stroke-width="1.5"/></svg>
      <span>100%</span>
      <div class="battery"><i></i></div>
    </div>
  </div>

  <div class="setting-row">
    <span class="setting-label">Pistol</span>
    <div class="option-group">
      <div class="option is-active"><svg viewBox="0 0 26 26"><path d="M4 8h18v4H12l-1 2H9l-1 6H5l1-7-2-1z" fill="#fff"/></svg></div>
      <div class="option"><svg viewBox="0 0 26 26"><path d="M2 11h20v2H13l-2 3h-2l1-3H6l-2 2H2z" fill="#fff"/></svg></div>
    </div>
  </div>

  <div class="setting-row">
    <span class="setting-label">Current Firearm</span>
    <span class="setting-value">K340</span>
  </div>

  <div class="setting-row">
    <span class="setting-label">Right Handed</span>
    <div class="option-group">
      <div class="option"><svg viewBox="0 0 26 26"><path d="M9 21c-3-2-5-5-6-8l2-1 3 3V6h2v7-9h2v9-8h2v8-6h2v10c0 4-2 6-5 6z" fill="#fff"/></svg></div>
      <div class="option is-active"><svg viewBox="0 0 26 26"><path d="M17 21c3-2 5-5 6-8l-2-1-3 3V6h-2v7-9h-2v9-8h-2v8-6H8v10c0 4 2 6 5 6z" fill="#fff"/></svg></div>
    </div>
  </div>

  <div class="setting-row">
    <span class="setting-label">Dry Practice</span>
    <div class="option-group">
      <div class="option"><svg viewBox="0 0 26 26"><path d="M10 20V10c0-3 1.5-5 3-6 1.5 1 3 3 3 6v10zM9 21h8v2H9z" fill="#fff"/></svg></div>
      <div class="option is-active"><svg viewBox="0 0 26 26"><rect x="10" y="3" width="6" height="15" rx="1" fill="#fff"/><rect x="10" y="20" width="6" height="3" fill="#fff"/></svg></div>
      <div class="option">CO<sub style="font-size:9px">2</sub></div>
    </div>
  </div>

  <div class="setting-row">
    <span class="setting-label">Device Mount Position</span>
    <div class="option-group">
      <div class="option"><svg viewBox="0 0 26 26"><path d="M13 21V5M7 11l6-6 6 6" fill="none" stroke="#fff" stroke-width="1.5"/></svg></div>
      <div class="option is-active"><svg viewBox="0 0 26 26"><path d="M13 5v16M7 15l6 6 6-6" fill="none" stroke="#fff" stroke-width="1.5"/></svg></div>
      <div class="option info">i</div>
    </div>
  </div>

  <div class="setting-row">
    <span class="setting-label">Device Mount Location</span>
    <div class="option-group">
      <div class="option is-active"><svg viewBox="0 0 26 26"><path d="M13 5v16M7 15l6 6 6-6" fill="none" stroke="#fff" stroke-width="1.5"/></svg></div>
      <div class="option"><svg viewBox="0 0 26 26"><path d="M13 21V5M7 11l6-6 6 6" fill="none" stroke="#fff" stroke-width="1.5"/></svg></div>
      <div class="option"><svg viewBox="0 0 26 26"><path d="M21 13H5M11 7l-6 6 6 6" fill="none" stroke="#fff" stroke-width="1.5"/></svg></div>
      <div class="option"><svg viewBox="0 0 26 26"><path d="M5 13h16M15 7l6 6-6 6" fill="none" stroke="#fff" stroke-width="1.5"/></svg></div>
      <div class="option info">i</div>
    </div>
  </div>

  <div class="setting-row">
    <span class="setting-label">Bullseye Mode</span>
    <div class="option-group">
      <div class="option is-active">OFF</div>
      <div class="option">ON</div>
      <div class="option info">i</div>
    </div>
  </div>

  <div class="link-row"><span>Logout [jorel]</span><svg viewBox="0 0 10 24"><path d="M2 2l6 10-6 10" fill="none" stroke="#888" stroke-width="1.2"/></svg></div>
  <div class="link-row"><span>Sync Account Data</span><svg viewBox="0 0 10 24"><path d="M2 2l6 10-6 10" fill="none" stroke="#888" stroke-width="1.2"/></svg></div>
  <div class="link-row"><span>Disconnect Bluetooth</span><svg viewBox="0 0 10 24"><path d="M2 2l6 10-6 10" fill="none" stroke="#888" stroke-width="1.2"/></svg></div>
  <div class="link-row"><span>Report Issue</span><svg viewBox="0 0 10 24"><path d="M2 2l6 10-6 10" fill="none" stroke="#888" stroke-width="1.2"/></svg></div>

  <div class="version-strip">App Version: 2.3.9.05</div>

  <nav class="tab-bar">
    <div class="tab">
      <svg viewBox="0 0 60 56"><g fill="none" stroke="#fff" stroke-width="2.5"><circle cx="30" cy="28" r="26"/><circle cx="30" cy="28" r="19"/><circle cx="30" cy="28" r="12"/><circle cx="30" cy="28" r="5"/></g></svg>
      <span>TRAIN</span>
    </div>
    <div class="tab">
      <svg viewBox="0 0 60 56"><g fill="none" stroke="#fff" stroke-width="2.5"><rect x="11" y="32" width="11" height="22"/><rect x="25" y="17" width="11" height="37"/><rect x="39" y="2" width="11" height="52"/></g></svg>
      <span>HISTORY</span>
    </div>
    <div class="tab">
      <svg viewBox="0 0 60 56"><g fill="none" stroke="#fff" stroke-width="2.5"><path d="M6 24l24-10 24 10-24 10z"/><path d="M16 29v11c8 5 20 5 28 0V29"/><path d="M50 26v14"/></g><circle cx="50" cy="42" r="2.5" fill="#fff"/></svg>
      <span>LEARN</span>
    </div>
    <div class="tab is-current">
      <svg viewBox="0 0 60 56"><g fill="none" stroke="#c4363c" stroke-width="2.5"><path d="M26 4h8l2 7 6 3 7-3 5 6-4 6 1 7 7 3v8l-7 2-3 6 3 7-6 5-6-4-7 2-2 7h-8l-2-7-6-2-6 4-6-5 3-7-3-6-7-2v-8l7-3 1-7-4-6 5-6 7 3 6-3z" transform="translate(30 28) scale(0.48) translate(-30 -28)"/><circle cx="30" cy="28" r="8"/></g></svg>
      <span>SETTINGS</span>
    </div>
  </nav>
</main>
</body>
</html>
```